Award-winnning Estate Agent needs a premium version of their 'For Sale' board design

We need a premium option for our 'For Sale' board design. We have a standard board that is attached to this brief, but were are looking to have a premium design version that we will use when selling exclusive properties. Our company name is Harbour Lane Estates and the name for this is exclusive selection is: 'The Harbour Collection'. The design needs to work with our current brand, but have a distinctive PREMIUM feel to it. I have uploaded the barnd guidelines and also some of the exisisting logo variations. We do NOT need a new logo but feel free to play around with colours, fonts, sizes etc. for the sign.

Target Market(s)

Property buyers & house hunters

Industry/Entity Type

Real Estate - Residential Property

Font styles to use
Sans Serif

Requirements
Must have
• A premium fee, must be square design, must be easy to read when driving past the sign
Nice to have
• I'm open ot ideas

```html
<!DOCTYPE html>
<html lang="en">
<head>
<meta charset="utf-8">
<title>Harbour Lane Estates – For Sale Board</title>
<link rel="stylesheet" href="https://fonts.googleapis.com/css2?family=Arimo:wght@400;700&family=Pinyon+Script&display=swap">
<style>
  :root {
    --sky: #29a9e0;
    --ocean: #1077bb;
    --navy: #2b3990;
    --white: #ffffff;
    --page: #ffffff;
  }
  html, body {
    margin: 0;
    padding: 0;
    width: 1200px;
    height: 1200px;
    overflow: hidden;
    background: var(--page);
  }
  .board {
    position: relative;
    width: 1200px;
    height: 1200px;
    font-family: "Arimo", Arial, sans-serif;
  }
  .board__shapes {
    position: absolute;
    inset: 0;
  }
  .brand-name {
    position: absolute;
    left: 0;
    right: 0;
    top: 470px;
    text-align: center;
    font-size: 84px;
    font-weight: 700;
    color: var(--navy);
    letter-spacing: -0.5px;
    line-height: 1;
  }
  .collection-name {
    position: absolute;
    left: 0;
    right: 0;
    top: 712px;
    text-align: center;
    font-family: "Pinyon Script", cursive;
    font-size: 66px;
    color: var(--white);
    line-height: 1;
  }
  .for-sale {
    position: absolute;
    left: 0;
    top: 780px;
  }
  .for-sale text {
    font-family: "Arimo", Arial, sans-serif;
    font-weight: 700;
    font-size: 178px;
    fill: var(--navy);
    stroke: var(--white);
    stroke-width: 10px;
    stroke-linejoin: round;
    paint-order: stroke fill;
  }
  .rule {
    position: absolute;
    left: 160px;
    width: 885px;
    height: 2px;
    background: var(--white);
  }
  .rule--top { top: 960px; }
  .rule--bottom { top: 1088px; }
  .contact-phone {
    position: absolute;
    left: 196px;
    top: 974px;
    display: flex;
    align-items: center;
    gap: 22px;
  }
  .contact-phone__icon {
    width: 100px;
    height: 100px;
    fill: var(--sky);
  }
  .contact-phone__number {
    font-size: 104px;
    font-weight: 700;
    color: var(--white);
    line-height: 1;
    letter-spacing: -1px;
  }
  .web-address {
    position: absolute;
    left: 0;
    right: 0;
    top: 1122px;
    text-align: center;
    font-size: 41px;
    font-weight: 400;
    color: var(--white);
    line-height: 1;
  }
</style>
</head>
<body>
  <main class="board">
    <svg class="board__shapes" width="1200" height="1200" viewBox="0 0 1200 1200" aria-hidden="true">
      <rect class="panel-sky" x="16" y="16" width="1168" height="1168" rx="7" fill="var(--sky)"/>
      <polygon class="panel-roof" points="16,251 600,27 1184,251 1184,822 601,581 16,822" fill="var(--white)"/>
      <path class="panel-house" d="M16 822 L601 581 L1184 822 L1184 1177 Q1184 1184 1177 1184 L23 1184 Q16 1184 16 1177 Z" fill="var(--ocean)"/>
    </svg>

    <div class="brand-name">Harbour Lane Estates</div>

    <div class="collection-name">The Harbour Collection</div>

    <svg class="for-sale" width="1200" height="180" viewBox="0 0 1200 180">
      <text x="604" y="156" text-anchor="middle" textLength="880" lengthAdjust="spacingAndGlyphs">FOR SALE</text>
    </svg>

    <div class="rule rule--top"></div>

    <div class="contact-phone">
      <svg class="contact-phone__icon" viewBox="0 0 24 24" aria-hidden="true">
        <path d="M6.6 10.8c1.4 2.8 3.8 5.1 6.6 6.6l2.2-2.2c.3-.3.7-.4 1-.2 1.1.4 2.3.6 3.6.6.6 0 1 .4 1 1V20c0 .6-.4 1-1 1C10.6 21 3 13.4 3 4c0-.6.4-1 1-1h3.5c.6 0 1 .4 1 1 0 1.3.2 2.5.6 3.6.1.3 0 .7-.2 1L6.6 10.8z"/>
      </svg>
      <span class="contact-phone__number">01632 960418</span>
    </div>

    <div class="rule rule--bottom"></div>

    <div class="web-address">www.harbourlaneestates.co.uk</div>
  </main>
</body>
</html>
```